Photoshop Templates for Instagram, x 2

A Square template to reuse that is on brand.

It will involve an image and text of between 3 and 10 words.
I would like 2 separate contrasting images to use interchangeably

In the files I have added some of the images that I have been using, as well as the home page of my website that is currently being developed.

The on brand would be very recognisable with the website.

Requirements
Must have
• Must be similar in feel to the home page.

Must be simple to to change image and and text in the template

I would like 2 designs. Both similar, but contrasting

The square images show the look that I have been using (created by myself, so I'm sure these can be massively improved upon)

```html
<!DOCTYPE html>
<html lang="en">
<head>
<meta charset="utf-8">
<title>Quote Post – Good Sport</title>
<link rel="stylesheet" href="https://fonts.googleapis.com/css2?family=Montserrat:wght@300;400;700;800&display=swap">
<style>
  :root {
    --ink: #000000;
    --paper: #ffffff;
    --blue-deep: #0a4f9a;
    --blue-mid: #1b8fe0;
    --blue-light: #5fd0f5;
    --sky-white: #f4fbff;
    --cloud-grey: #9aa6b2;
  }
  html, body {
    margin: 0;
    padding: 0;
    width: 1200px;
    height: 1200px;
    overflow: hidden;
    background: var(--ink);
  }
  .post {
    position: relative;
    width: 1200px;
    height: 1200px;
    background: var(--ink);
    overflow: hidden;
    font-family: "Montserrat", sans-serif;
  }
  .post__art {
    position: absolute;
    inset: 0;
  }
  .quote {
    position: absolute;
    right: 36px;
    top: 640px;
    margin: 0;
    text-align: right;
    color: var(--paper);
    font-weight: 400;
    font-size: 60px;
    line-height: 70px;
    letter-spacing: 0.5px;
    text-transform: uppercase;
  }
  .quote__line { display: block; }
  .attribution {
    position: absolute;
    right: 28px;
    top: 1072px;
    margin: 0;
    color: var(--paper);
    font-weight: 800;
    font-size: 46px;
    letter-spacing: 0.5px;
    text-transform: uppercase;
  }
</style>
</head>
<body>
  <main class="post">
    <svg class="post__art" width="1200" height="1200" viewBox="0 0 1200 1200">
      <defs>
        <linearGradient id="photo-tone" x1="0" y1="1" x2="1" y2="0">
          <stop offset="0" stop-color="var(--blue-deep)"/>
          <stop offset="0.35" stop-color="var(--blue-mid)"/>
          <stop offset="0.6" stop-color="var(--blue-light)"/>
          <stop offset="0.78" stop-color="var(--sky-white)"/>
          <stop offset="1" stop-color="var(--cloud-grey)"/>
        </linearGradient>
        <linearGradient id="edge-fade" x1="0" y1="0" x2="1" y2="0">
          <stop offset="0" stop-color="#000" stop-opacity="0.85"/>
          <stop offset="0.12" stop-color="#000" stop-opacity="0"/>
        </linearGradient>
        <clipPath id="photo-shape">
          <polygon points="328,0 1176,0 1176,276 252,1200 0,1200 0,312"/>
        </clipPath>
      </defs>

      <g class="photo-window" clip-path="url(#photo-shape)">
        <rect class="photo-placeholder" role="img"
              aria-label="Athlete in profile wearing goalkeeper gloves against a bright cloudy sky, toned blue"
              x="0" y="0" width="1200" height="1200" fill="url(#photo-tone)"/>
        <g class="light-bands" fill="var(--paper)">
          <polygon points="660,112 920,112 700,332 440,332" opacity="0.12"/>
          <polygon points="120,290 500,290 290,500 -90,500" opacity="0.1"/>
          <polygon points="60,580 420,580 290,710 -70,710" opacity="0.08"/>
        </g>
        <g class="shade-bands" fill="var(--blue-deep)">
          <polygon points="290,580 700,580 560,720 150,720" opacity="0.25"/>
          <polygon points="90,900 560,900 360,1060 -110,1060" opacity="0.3"/>
        </g>
        <rect class="edge-fade" x="0" y="0" width="1200" height="1200" fill="url(#edge-fade)"/>
      </g>
    </svg>

    <blockquote class="quote">
      <span class="quote__line">“The</span>
      <span class="quote__line">only way</span>
      <span class="quote__line">to prove you</span>
      <span class="quote__line">are a good</span>
      <span class="quote__line">sport</span>
      <span class="quote__line">is to lose”</span>
    </blockquote>
    <p class="attribution">– Marcus Hale</p>
  </main>
</body>
</html>
```